Brightwire Hollow Business cards

one side I would like my logo (uploaded) and the other side I want my details. I'm an electrician in sydney. The logo side I'm happy with just a white background and our logo in the middle.

Details for other side
24/7 Sydney Electrician
Marcus Pell
0431 587 219
marcus@brightwirehollow.com.au
brightwirehollow.com.au
icons for facebook, instagram, linked in

Industry/Entity Type

electrician

Contact Information for Business Card

company info

```html
<!DOCTYPE html>
<html lang="en">
<head>
<meta charset="utf-8">
<title>Brightwire Hollow – Business Cards</title>
<link rel="stylesheet" href="https://fonts.googleapis.com/css2?family=Exo+2:wght@400;700&display=swap">
<style>
  :root {
    --stage: #2a2a2b;
    --paper-white: #fbfbfb;
    --paper-black: #141414;
    --brand-red: #ec0f0f;
    --ink-light: #ececec;
    --ink-dark: #111111;
  }
  * { box-sizing: border-box; margin: 0; padding: 0; }
  html, body {
    width: 1200px;
    height: 800px;
    overflow: hidden;
    background: var(--stage);
  }
  .stage {
    width: 1200px;
    height: 800px;
    display: flex;
    align-items: center;
    justify-content: center;
    gap: 40px;
  }
  .card {
    position: relative;
    width: 540px;
    height: 346px;
    overflow: hidden;
  }
  .card--front {
    background: var(--paper-white);
    display: flex;
    align-items: center;
    justify-content: center;
  }
  .brand-name {
    font-family: "Exo 2", sans-serif;
    font-weight: 700;
    font-size: 40px;
    letter-spacing: 1px;
    color: var(--brand-red);
    text-transform: uppercase;
  }
  .card--back {
    background: var(--paper-black);
    font-family: "Exo 2", sans-serif;
  }
  .contact-list {
    list-style: none;
    position: absolute;
    left: 52px;
    top: 58px;
  }
  .contact-item {
    display: flex;
    align-items: center;
    gap: 6px;
    height: 26px;
    margin-bottom: 26.5px;
    font-size: 18px;
    font-weight: 400;
    letter-spacing: 2.2px;
    color: var(--ink-light);
  }
  .contact-icon {
    width: 14px;
    height: 14px;
    flex: none;
    fill: var(--brand-red);
  }
  .social-links {
    position: absolute;
    right: 52px;
    top: 217px;
    display: flex;
    gap: 16px;
  }
  .social-dot {
    width: 12px;
    height: 12px;
    border-radius: 50%;
    background: var(--brand-red);
  }
  .tagline-band {
    position: absolute;
    left: 0;
    bottom: 0;
    width: 540px;
    height: 42px;
  }
  .tagline {
    position: absolute;
    left: 0;
    right: 0;
    bottom: 12px;
    text-align: center;
    font-size: 16px;
    font-weight: 700;
    letter-spacing: 2.4px;
    color: var(--ink-dark);
  }
</style>
</head>
<body>
<main class="stage">
  <section class="card card--front" aria-label="Business card front">
    <span class="brand-name">Brightwire Hollow</span>
  </section>

  <section class="card card--back" aria-label="Business card back">
    <ul class="contact-list">
      <li class="contact-item">
        <svg class="contact-icon" viewBox="0 0 16 16" aria-hidden="true">
          <circle cx="8" cy="4.5" r="3.5"/>
          <path d="M1.5 16v-2.5c0-3 2.8-5 6.5-5s6.5 2 6.5 5V16z"/>
        </svg>
        Marcus Pell
      </li>
      <li class="contact-item">
        <svg class="contact-icon" viewBox="0 0 16 16" aria-hidden="true">
          <path d="M3.6 1 6 3.6 4.6 5.4c.9 2 2.4 3.6 4.4 4.6l1.8-1.5L15 11l-.9 3c-.3.8-1.1 1.2-1.9 1C6.6 13.6 2.4 9.4 1 3.8.8 3 1.2 2.2 2 1.9z"/>
        </svg>
        0431 587 219
      </li>
      <li class="contact-item">
        <svg class="contact-icon" viewBox="0 0 16 16" aria-hidden="true">
          <path d="M1 3h14v10H1zM2.2 4.2 8 8.6l5.8-4.4v-.1H2.2z" fill-rule="evenodd"/>
        </svg>
        marcus@brightwirehollow.com.au
      </li>
      <li class="contact-item">
        <svg class="contact-icon" viewBox="0 0 16 16" aria-hidden="true">
          <path d="M8 1a7 7 0 1 0 0 14A7 7 0 0 0 8 1zm-.8 1.7v4.5H4.6c.1-2 1.1-3.8 2.6-4.5zm1.6 0c1.5.7 2.5 2.5 2.6 4.5H8.8zM7.2 8.8v4.5c-1.5-.7-2.5-2.5-2.6-4.5zm1.6 0h2.6c-.1 2-1.1 3.8-2.6 4.5z"/>
        </svg>
        brightwirehollow.com.au
      </li>
    </ul>

    <div class="social-links" aria-label="Social profiles">
      <span class="social-dot"></span>
      <span class="social-dot"></span>
      <span class="social-dot"></span>
    </div>

    <svg class="tagline-band" viewBox="0 0 540 42" aria-hidden="true">
      <polygon fill="var(--brand-red)" points="0,29 120,29 136,0 404,0 420,29 540,29 540,42 0,42"/>
    </svg>
    <p class="tagline">24/7 SYDNEY ELECTRICIAN</p>
  </section>
</main>
</body>
</html>
```